Ferncastle Holdings - stationery for luxury, exclusive property investment company

We need stationery (letterhead, folder, compliments slip and envelope) and business cards which will reflect our luxury brand.

I have attached some design examples that we like.

We are an investment company which buys property to provide accommodation for corporate customers.

The design of the stationery needs to be be simple, refined, understated, luxury and very tasteful.

The design should communicate luxury and exclusivity, without being ostentatious.

Logo files are attached

Please can designers re-read the brief, and make sure the logo is in gold on either on a navy or white background.

Target Market(s)

Wealthy customers

Contact Information for Business Card

Helen Travers-Booth
Director
Ferncastle Holdings Limited
email: helen@ferncastleholdings.co.uk
mob: 07712645930

Font styles to use
Serif

Colors

Designer to choose colors to be used in the design.

Requirements
Must have
• The logo must be gold on either a white or navy background as per the attached logos.
• The stationery MUST have the following information:
• Ferncastle Holdings Limited
• The Willows
• Ashby Rise
• Ashby
• GL52 7TN
• Company Number: 20418736 (Registered in England and Wales)
• The letterhead must also have the two attached logos for the PLG and the PLG accreditation scheme. They do not need to be large.
Nice to have
• A watermark, navy banding either top or bottom.
Should not have
• Anything that looks budget.

```html
<!DOCTYPE html>
<html lang="en">
<head>
<meta charset="utf-8">
<title>Ferncastle Holdings – Presentation Folder</title>
<link rel="stylesheet" href="https://fonts.googleapis.com/css2?family=Jost:wght@300;400&display=swap">
<style>
  :root {
    --navy: #02012d;
    --gold: #c9a464;
    --gold-soft: #d8bd8a;
    --paper: #ebecee;
    --paper-light: #f3f3f4;
    --fold: #d6d7da;
    --label: #b9b9b9;
    --canvas: #ffffff;
  }
  html, body {
    margin: 0;
    padding: 0;
    width: 1200px;
    height: 609px;
    overflow: hidden;
    background: var(--canvas);
    font-family: "Jost", sans-serif;
  }
  .sheet {
    position: relative;
    width: 1200px;
    height: 609px;
  }
  .folder-cover {
    position: absolute;
    left: 0;
    top: 0;
    width: 407px;
    height: 578px;
    background: var(--navy);
  }
  .brand {
    position: absolute;
    left: 0;
    width: 407px;
    top: 300px;
    text-align: center;
    color: var(--gold);
  }
  .brand-name {
    font-weight: 400;
    font-size: 19px;
    letter-spacing: 3px;
    text-transform: uppercase;
    color: var(--gold);
    line-height: 1;
  }
  .brand-registration {
    margin-top: 22px;
    font-weight: 300;
    font-size: 6.5px;
    line-height: 10px;
    color: var(--gold-soft);
  }
  .folder-inside {
    position: absolute;
    left: 422px;
    top: 0;
    width: 778px;
    height: 576px;
    overflow: hidden;
    border: 1px solid var(--fold);
    box-sizing: border-box;
  }
  .inside-pattern {
    position: absolute;
    inset: 0;
    background:
      radial-gradient(ellipse 260px 230px at 90px 70px, rgba(225, 250, 255, 0.95), rgba(225, 250, 255, 0) 75%),
      linear-gradient(180deg, var(--paper-light), var(--paper));
  }
  .fold-line {
    position: absolute;
    left: 389px;
    top: 0;
    width: 1px;
    height: 100%;
    background: var(--fold);
  }
  .pocket {
    position: absolute;
    left: 389px;
    top: 360px;
    width: 389px;
    height: 216px;
  }
  .pocket-address {
    position: absolute;
    right: 22px;
    bottom: 31px;
    font-weight: 300;
    font-size: 8.6px;
    color: #e4e4ea;
    white-space: nowrap;
  }
  .panel-label {
    position: absolute;
    top: 586px;
    font-weight: 300;
    font-size: 18px;
    color: var(--label);
  }
  .panel-label.cover { left: 171px; }
  .panel-label.inside { left: 788px; }
</style>
</head>
<body>
<main class="sheet">
  <section class="folder-cover">
    <div class="brand">
      <div class="brand-name">Ferncastle Holdings</div>
      <div class="brand-registration">Company Number: 20418736<br>(Registered in England and Wales)</div>
    </div>
  </section>

  <section class="folder-inside">
    <div class="inside-pattern" role="img" aria-label="Soft grey honeycomb pattern with glowing hexagons at top left"></div>
    <div class="fold-line"></div>
    <svg class="pocket" width="389" height="216" viewBox="0 0 389 216" aria-hidden="true">
      <defs>
        <filter id="pocket-shadow" x="-10%" y="-30%" width="120%" height="160%">
          <feGaussianBlur stdDeviation="7"/>
        </filter>
      </defs>
      <polygon points="120,14 389,14 389,216 0,216" fill="#000" opacity="0.28" filter="url(#pocket-shadow)"/>
      <polygon points="119,18 389,18 389,216 0,216" fill="var(--navy)"/>
    </svg>
    <div class="pocket-address">Ferncastle Holdings Limited • The Willows • Ashby Rise • Ashby • GL52 7TN</div>
  </section>

  <div class="panel-label cover">Cover</div>
  <div class="panel-label inside">Inside</div>
</main>
</body>
</html>
```